Electrical & Communications Company Wordpress Themed Website Design

Hi everyone,

I need a wordpress themed website designed for a new company based in Sydney Australia called "TRELVEX". It delivers electrical and communication services to the domestic and commercial sectors.

It needs to be the FULL/COMPLETE wordpress theme! A clean and easy to use site.

Please guys take the time to look at these competitors sites:

www.quobble.com.au
www.zirconvoltworks.com.au
www.ubt.com.au
www.tallowwiring.com.au
www.wrightbergwire.com.au
www.gullivarwiremen.com.au

Please use these site for ideas only!!! we want to be original.

(If you would like to add electrical and communications to the logo that is O.K.)

Note: These logo's are registered trademarks of trelvex pty ltd.

Accreditation:

Bufo member (United cabling and signalling trades guild)

PLEASE CHECK THE WEB PLANNING LAYOUT BELOW FOR ROUGH IDEA

Have requested to increase payment to $400 and now guarantee payment!

Hi guys, forgot to mention i would like to see the business phone number prominently some where with a call to action.As we are a service business and need people to easly be able to see our contact number. Maybe top right courner but open to ideas. 

 Guys/Girls this is for a complete working word press theme that i can load up on the sever and access thru wordpress admin. Code etc

• - Logo Provided must be used
• - Themes and colours to be consisted with with brand
• - Fully customizable
• - Have a social share button from pinquo.com
• - Must be the full/complete theme for word press
• - zenpixbanks
• - contactform
• - would like orbe lumo charge bitfen displayed
• - Guarantee logo or something
• - Please don't waste your or our time submitting templates or copies of other sites original only!

```html
<!DOCTYPE html>
<html lang="en">
<head>
<meta charset="utf-8">
<title>Trelvex – Electrical &amp; Communications</title>
<link rel="stylesheet" href="https://fonts.googleapis.com/css2?family=Questrial&family=Arimo:wght@400;700&display=swap">
<style>
  :root {
    --page-black: #000000;
    --panel-dark: #16171d;
    --header-light: #fbfbfb;
    --header-grey: #b9b9bb;
    --brand-red: #e3141e;
    --nav-red-top: #d71e0c;
    --nav-red-bottom: #b21004;
    --home-red: #c71a06;
    --text-white: #f2f2f2;
    --heading-grey: #d9d9d9;
    --body-grey: #7a7a7e;
    --button-grey: #d4d4d4;
    --button-dark: #2b2b2b;
    --footer-border: #8fb4d6;
  }
  * { box-sizing: border-box; margin: 0; padding: 0; }
  html, body {
    width: 1200px; height: 1064px; overflow: hidden;
    background: var(--page-black);
    font-family: "Arimo", Arial, sans-serif;
  }
  .canvas { position: relative; width: 1200px; height: 1064px; }
  .panel {
    position: absolute; left: 27px; top: 0; width: 1143px; height: 1013px;
    background: var(--panel-dark);
  }

  /* Header */
  .site-header {
    position: absolute; left: 57px; top: 0; width: 1079px; height: 109px;
    background: linear-gradient(#ffffff 0%, var(--header-light) 35%, var(--header-grey) 100%);
    border-radius: 0 0 15px 15px;
  }
  .brand {
    position: absolute; left: 6px; top: 22px;
    display: flex; align-items: center; gap: 10px;
  }
  .brand-dot { width: 34px; height: 34px; border-radius: 50%; background: var(--brand-red); }
  .brand-name {
    font-family: "Questrial", sans-serif; font-size: 44px; color: var(--brand-red);
    letter-spacing: 1px; line-height: 1;
  }
  .call-button {
    position: absolute; left: 831px; top: 25px; width: 227px; height: 56px;
    border-radius: 9px; border: 1px solid #c50f18;
    background: linear-gradient(#ff3a45, #e8121d 55%, #d50d17);
    display: flex; align-items: center; padding-left: 18px; gap: 14px;
  }
  .call-number {
    font-family: "Arimo", sans-serif; font-weight: 700; font-size: 22px;
    color: #fff; letter-spacing: 1px;
  }

  /* Navigation */
  .main-nav {
    position: absolute; left: 60px; top: 136px; width: 1076px; height: 46px;
    border-radius: 7px;
    background: linear-gradient(var(--nav-red-top), var(--nav-red-bottom));
  }
  .main-nav a {
    position: absolute; top: 0; line-height: 46px;
    font-family: "Arimo", sans-serif; font-size: 16px; letter-spacing: 1px;
    color: var(--text-white); text-decoration: none;
  }
  .main-nav a.is-current {
    top: 9px; height: 32px; line-height: 32px; padding: 0 12px;
    background: var(--home-red); font-weight: 700; font-size: 15px;
    box-shadow: inset 0 0 6px rgba(0,0,0,.25);
  }

  /* Hero */
  .hero-photo {
    position: absolute; left: 403px; top: 182px; width: 767px; height: 373px;
    background:
      radial-gradient(ellipse 220px 150px at 400px 150px, rgba(255,214,120,.95), rgba(230,110,30,.55) 40%, rgba(80,25,10,.2) 75%, transparent 100%),
      linear-gradient(120deg, #1a0d08, #050303 60%, #120a06);
  }
  .social-links { position: absolute; top: 207px; left: 992px; display: flex; gap: 22px; }
  .social-links span { width: 32px; height: 32px; border-radius: 4px; display: block; }
  .social-feed { background: #ee7d1a; }
  .social-bird { background: #3fb4e6; }
  .social-book { background: #3b5a9a; }
  .view-more {
    position: absolute; left: 986px; top: 493px; width: 137px; height: 41px;
    border-radius: 12px; background: linear-gradient(#f0f0f0, #bdbdbd);
    font-family: "Arimo", sans-serif; font-weight: 700; font-size: 17px;
    color: var(--button-dark); text-align: center; line-height: 41px;
  }

  .slider-frame {
    position: absolute; left: 61px; top: 216px; width: 571px; height: 314px;
    border-radius: 17px; background: #fff; border: 3px solid #f5dbe6;
  }
  .slide {
    position: absolute; left: 10px; top: 12px; width: 544px; height: 284px; overflow: hidden;
  }
  .slide-top { height: 75px; background: linear-gradient(#3c3f3f, #1e2120); }
  .slide-band { height: 8px; background: #c5102d; }
  .slide-image {
    height: 201px;
    background:
      radial-gradient(circle at 80px 170px, rgba(255,220,230,.9), transparent 120px),
      linear-gradient(#e2184c, #d41237 60%, #c10f2c);
  }
  .slide-title {
    position: absolute; left: 53px; top: 118px;
    font-family: "Questrial", sans-serif; font-size: 36px; line-height: 52px;
    letter-spacing: 3px; color: #fff;
  }
  .slider-arrow {
    position: absolute; width: 30px; height: 30px; border-radius: 50%;
    background: #f4f4f4; border: 1px solid #bbb;
  }

  /* Content */
  .section-title {
    font-family: "Questrial", sans-serif; font-weight: 400;
    color: var(--heading-grey); letter-spacing: 3px;
  }
  .section-title em { font-style: normal; color: var(--brand-red); }
  .welcome { position: absolute; left: 60px; top: 550px; width: 1070px; }
  .welcome .section-title { font-size: 30px; }
  .body-text { font-size: 13.5px; line-height: 23px; color: var(--body-grey); margin-top: 10px; }

  .feature { position: absolute; top: 710px; width: 340px; }
  .feature .section-title { font-size: 28px; height: 40px; }
  .feature .body-text { margin-top: 10px; }
  .more-button {
    margin-top: 12px; width: 68px; height: 19px; border-radius: 4px;
    background: linear-gradient(#f2f2f2, #bcbcbc);
    font-size: 12px; color: #222; display: flex; align-items: center; justify-content: center; gap: 4px;
  }

  /* Footer */
  .site-footer {
    position: absolute; left: 60px; top: 939px; width: 1076px; height: 57px;
    border-radius: 9px; border: 1px solid var(--footer-border);
    background: linear-gradient(#ffffff, #dedede 60%, #bdbdbd);
  }
  .copyright {
    position: absolute; left: 27px; top: 0; line-height: 57px;
    font-size: 13.5px; letter-spacing: 1px; color: #444;
  }
  .footer-brand {
    position: absolute; right: 22px; top: 13px; display: flex; align-items: center; gap: 7px;
  }
  .footer-brand .brand-dot { width: 22px; height: 22px; }
  .footer-brand .brand-name { font-size: 28px; }
</style>
</head>
<body>
<div class="canvas">
  <div class="panel"></div>

  <header class="site-header">
    <div class="brand"><span class="brand-dot"></span><span class="brand-name">TRELVEX</span></div>
    <div class="call-button">
      <svg width="22" height="34" viewBox="0 0 22 34" aria-hidden="true">
        <rect x="2" y="2" width="18" height="30" rx="6" fill="#f4f4f4" stroke="#bbb"/>
        <rect x="6" y="9" width="10" height="10" rx="2" fill="#37c35a"/>
        <circle cx="11" cy="25" r="2.5" fill="#999"/>
      </svg>
      <span class="call-number">000-000-0000</span>
    </div>
  </header>

  <nav class="main-nav">
    <a class="is-current" style="left:22px">Home</a>
    <a style="left:111px">About Us</a>
    <a style="left:214px">Services</a>
    <a style="left:312px">Recent Jobs</a>
    <a style="left:443px">Experience</a>
    <a style="left:557px">Our Process</a>
    <a style="left:689px">Quotes</a>
    <a style="left:774px">FAQ</a>
    <a style="left:835px">Blog</a>
    <a style="left:897px">Contact Us</a>
  </nav>

  <div class="hero-photo" role="img" aria-label="Photo of stripped copper wires sparking with a bright electric arc"></div>
  <div class="social-links">
    <span class="social-feed" aria-label="News feed"></span>
    <span class="social-bird" aria-label="Social link"></span>
    <span class="social-book" aria-label="Social link"></span>
  </div>
  <div class="view-more">VIEW MORE</div>

  <div class="slider-frame">
    <div class="slide">
      <div class="slide-top"></div>
      <div class="slide-band"></div>
      <div class="slide-image" role="img" aria-label="Red background with soft pink light bokeh"></div>
      <div class="slide-title">Electrical Service with<br>Satisfaction</div>
    </div>
  </div>
  <div class="slider-arrow" style="left:50px;top:362px">
    <svg width="28" height="28" viewBox="0 0 28 28" aria-hidden="true"><path d="M11 7h6v8h4l-7 7-7-7h4z" fill="#333"/></svg>
  </div>
  <div class="slider-arrow" style="left:613px;top:361px">
    <svg width="28" height="28" viewBox="0 0 28 28" aria-hidden="true"><path d="M11 21h6v-8h4l-7-7-7 7h4z" fill="#333"/></svg>
  </div>

  <section class="welcome">
    <h1 class="section-title">Welcome&nbsp; to <em>Trelvex</em></h1>
    <p class="body-text">Nunc eleifend, enim nec posuere posuere, dui dolor interdum orci, non luctus pede felis a eros. Ut feugiat, magna id bibendum vehicula, ante eros ultricies metus, imperdiet consequat quam dolor non lorem. Curabitur dignissim, purus id posuere vehicula, ipsum risus placerat lacus, vel interdum enim augue at augue. Sed iaculis enim in lacus. Sed consequat ornare quam. Vivamus pulvinar sollicitudin metus. Vivamus id risus sed pede convallis fringilla.</p>
  </section>

  <section class="feature" style="left:57px">
    <h2 class="section-title">Our <em>Services</em></h2>
    <p class="body-text">Praesent in velit sit amet dolor gravida fringilla. Maecenas feugiat metus sed pede. Morbi cursus vestibulum neque. Etiam accumsan arcu placerat leo.</p>
    <div class="more-button">more <svg width="6" height="8" aria-hidden="true"><path d="M0 0l6 4-6 4z" fill="#222"/></svg></div>
  </section>
  <section class="feature" style="left:425px">
    <h2 class="section-title">Our <em>Recent Jobs</em></h2>
    <p class="body-text">Praesent in velit sit amet dolor gravida fringilla. Maecenas feugiat metus sed pede. Morbi cursus vestibulum neque. Etiam accumsan arcu placerat leo.</p>
    <div class="more-button">more <svg width="6" height="8" aria-hidden="true"><path d="M0 0l6 4-6 4z" fill="#222"/></svg></div>
  </section>
  <section class="feature" style="left:792px">
    <h2 class="section-title">Our <em>Experience</em></h2>
    <p class="body-text">Praesent in velit sit amet dolor gravida fringilla. Maecenas feugiat metus sed pede. Morbi cursus vestibulum neque. Etiam accumsan arcu placerat leo.</p>
    <div class="more-button">more <svg width="6" height="8" aria-hidden="true"><path d="M0 0l6 4-6 4z" fill="#222"/></svg></div>
  </section>

  <footer class="site-footer">
    <p class="copyright">copyright@trelvex 2010</p>
    <div class="footer-brand"><span class="brand-dot"></span><span class="brand-name">TRELVEX</span></div>
  </footer>
</div>
</body>
</html>
```